Pelican Global Trade & Heritage Forum Landing Page Design

We are a Chinese high-end bespoke business travel company. We want to design a landing page, to promote our brand and business, to attract target clients for business development.

We have own logo, like design in modern simple style, like to sample as attached. Like the Sample 2, use different color to display our business services.

We want to mainly display 7 parts of business:
1. Visa Services
2. International Hotel Reservation
3. Worldwide Flight Tickets Booking
4. Worldwide Travel Arrangement
5. VIP Airport Concierge
6. Duty Free Goods
7. International Business Resources

We imagine design a world map, points out popular countries, cities, and destinations, and combine with our own business resources cities.

Design in modern, business, international style. Thank you. Look forward to cooperate with you.

Target Market(s)

Business Clients and High income private client

Industry/Entity Type

Tourism, Business Travel, International Exchange

Coding

Coded - Design and coding required

Requirements
Must have
• Our logo, large images, design a world map

```html
<!DOCTYPE html>
<html lang="en">
<head>
<meta charset="utf-8">
<title>Pelican Global Trade &amp; Heritage Forum — Business Travel</title>
<link href="https://fonts.googleapis.com/css2?family=Inter:wght@400;500;600;700&display=swap" rel="stylesheet">
<style>
:root{
  --page-bg:#9cc1fd;
  --card-bg:#ffffff;
  --navy:#0b3a8f;
  --accent:#2f7fe8;
  --ink:#222;
  --muted:#555;
  --dark:#161616;
  --dark-2:#232323;
  --star:#00b67a;
  --orange:#e98a1c;
  --purple:#7a4cc9;
  --green:#6aa83a;
  --teal:#159aa5;
  --red:#d63b14;
  --gold:#d9a010;
  --pink:#d9356b;
  --sky:#5aa0e0;
  --soft:#eef4fd;
}
*{box-sizing:border-box;margin:0;padding:0}
html,body{width:1200px;height:2761px;overflow:hidden}
body{background:var(--page-bg);font-family:'Inter',sans-serif;color:var(--ink);position:relative}
.page{position:absolute;left:77px;top:89px;width:1045px;height:2584px;background:var(--card-bg);overflow:hidden}
.abs{position:absolute}
.btn{position:absolute;display:flex;align-items:center;justify-content:space-between;padding:0 18px 0 20px;border-radius:14px;background:var(--navy);color:#fff;font-size:10px;font-weight:500}
.btn svg{width:10px;height:10px}
/* header */
.brand{position:absolute;display:flex;align-items:center;gap:8px}
.brand-mark{width:46px;height:46px;border-radius:50%;background:var(--accent)}
.brand-name{color:var(--navy);font-weight:700;font-size:12px;line-height:1.25;width:150px}
.nav{position:absolute;left:511px;top:26px;display:flex;gap:0;font-size:10px;color:#222}
.nav span{position:absolute;white-space:nowrap}
/* hero */
.hero-title{position:absolute;left:83px;top:165px;font-size:40px;line-height:51px;font-weight:700;color:var(--navy);letter-spacing:-.3px}
.hero-text{position:absolute;left:83px;top:285px;width:340px;font-size:11px;line-height:19px;color:#444}
.stars{position:absolute;left:86px;top:474px;display:flex;gap:6px}
.stars i{width:18px;height:18px;background:var(--star);display:block;position:relative}
.stars i:after{content:"";position:absolute;left:4px;top:4px;width:10px;height:10px;background:#fff;clip-path:polygon(50% 0,61% 35%,98% 35%,68% 57%,79% 91%,50% 70%,21% 91%,32% 57%,2% 35%,39% 35%)}
.rating{position:absolute;left:86px;top:498px;font-size:12px;font-weight:600}
.rating b{color:var(--star);font-weight:600;text-decoration:underline}
.photo{position:absolute;border-radius:50%}
/* services */
.services{position:absolute;left:0;top:597px;width:1045px;height:690px;background:radial-gradient(ellipse at 10% 100%,#3a3a3a 0,var(--dark) 35%);color:#fff}
.kicker{position:absolute;width:100%;text-align:center;font-size:10px;font-weight:600;letter-spacing:1px}
.section-title{position:absolute;width:100%;text-align:center;font-size:18px;font-weight:700}
.svc-icon{position:absolute;width:86px;height:86px;margin:-43px 0 0 -43px;border-radius:50%;display:flex;align-items:center;justify-content:center}
.svc-icon div{width:58px;height:58px;border-radius:50%;display:flex;align-items:center;justify-content:center}
.svc-icon svg{width:30px;height:30px;fill:none;stroke:#fff;stroke-width:2;stroke-linecap:round;stroke-linejoin:round}
.svc{position:absolute;width:190px}
.svc h3{font-size:14px;font-weight:600;line-height:19px;margin-bottom:6px}
.svc p{font-size:11px;line-height:19px;color:#eee}
/* map */
.map-sec{position:absolute;left:0;top:1287px;width:1045px;height:651px;background-color:#fff;background-image:linear-gradient(#eef0f3 1px,transparent 1px),linear-gradient(90deg,#eef0f3 1px,transparent 1px);background-size:76px 76px;background-position:0 0,-1px 0}
.map-area{position:absolute;left:30px;top:124px;width:782px;height:418px;border-radius:40% 30% 45% 35%/40% 35% 50% 45%;background:linear-gradient(100deg,#8a5bd6 0%,#7e4fc9 20%,#6bb040 30%,#e6a23a 45%,#5aa0e0 50%,#e3507d 65%,#ec6d9b 80%,#eb9a3d 95%);opacity:.85}
.view{position:absolute;display:flex;flex-direction:column;align-items:center;color:#fff;font-size:11px;gap:2px}
.view i{width:22px;height:22px;border-radius:50%;background:rgba(255,255,255,.85);display:block}
.legend{position:absolute;left:846px;top:197px}
.legend div{display:flex;align-items:center;gap:14px;height:47px;font-size:17px;font-weight:500}
.legend svg{width:24px;height:34px}
/* testimonials */
.testi{position:absolute;left:0;top:1938px;width:1045px;height:337px;background:var(--dark);color:#fff}
.t-card{position:absolute;top:112px;width:228px;height:177px;background:var(--soft);border-radius:4px;color:var(--ink);padding:14px 26px}
.t-head{display:flex;gap:8px;align-items:center;margin-bottom:12px}
.avatar{width:44px;height:44px;border-radius:50%;background:linear-gradient(135deg,#6d5a4c,#2b2220)}
.t-name{font-size:17px;font-weight:500;line-height:21px}
.t-role{font-size:14px;color:var(--accent)}
.t-card p{font-size:11px;line-height:16px;color:#333}
.quote{position:absolute;left:194px;top:155px;width:54px;height:54px;border-radius:50%;background:var(--accent);display:flex;align-items:center;justify-content:center;font-size:34px;font-weight:700;color:#fff;line-height:1}
/* footer */
.footer{position:absolute;left:0;top:2275px;width:1045px;height:309px}
.f-text{position:absolute;left:51px;top:142px;width:250px;font-size:11px;line-height:16px;color:#333}
.f-col{position:absolute;top:50px;height:180px;border-left:3px solid var(--accent);background:linear-gradient(90deg,#f3f5f8,transparent 2px)}
.f-head{position:absolute;font-size:12px;font-weight:500}
.f-link{position:absolute;font-size:11px;color:#333}
.social{position:absolute;top:268px;left:54px;display:flex;gap:20px;font-size:11px;align-items:center}
.social span{display:flex;align-items:center;gap:6px}
.social i{width:16px;height:16px;background:var(--accent);display:block;border-radius:2px}
.copy{position:absolute;right:59px;top:269px;font-size:11px;color:#333}
</style>
</head>
<body>
<main class="page">

  <!-- header -->
  <div class="brand" style="left:64px;top:16px">
    <div class="brand-mark"></div>
    <div class="brand-name">Pelican Global Trade &amp; Heritage Forum</div>
  </div>
  <nav class="nav">
    <span style="left:0;top:0">Home</span>
    <span style="left:52px;top:0">Services ⌄</span>
    <span style="left:123px;top:0">Worldmap ⌄</span>
    <span style="left:205px;top:0">Blog</span>
    <span style="left:249px;top:0">Destinations</span>
  </nav>
  <a class="btn" style="left:834px;top:19px;width:145px;height:28px">Book your travel <svg viewBox="0 0 10 10"><path d="M3 1l4 4-4 4" stroke="#fff" stroke-width="1.6" fill="none"/></svg></a>

  <!-- hero -->
  <h1 class="hero-title">Smartest Way To<br>Business Travel</h1>
  <p class="hero-text">Lorem ipsum dolor sit amet consectetur adipiscing elit Ut et massa mi. Aliquam in hendrerit urna. Pellentesque sit amet sapien fringilla, quis nostrud exercitation</p>
  <a class="btn" style="left:83px;top:360px;width:145px;height:27px">Book your travel <svg viewBox="0 0 10 10"><path d="M3 1l4 4-4 4" stroke="#fff" stroke-width="1.6" fill="none"/></svg></a>
  <div class="stars"><i></i><i></i><i></i><i></i><i></i></div>
  <div class="rating">5.0 Rated on <b>TrustMeter</b></div>

  <svg class="abs" style="left:520px;top:100px" width="525" height="500" viewBox="0 0 525 500">
    <path d="M60 370 A270 270 0 0 1 500 80" fill="none" stroke="#9cc4ee" stroke-width="2" stroke-dasharray="14 10"/>
    <circle cx="292" cy="261" r="230" fill="#f1f6fd"/>
    <circle cx="292" cy="290" r="150" fill="#a9d4f2"/>
    <circle cx="505" cy="480" r="26" fill="#cfcfcf"/>
  </svg>
  <div class="abs" role="img" aria-label="Smiling businessman in a camel coat carrying travel bags" style="left:705px;top:142px;width:280px;height:455px;background:linear-gradient(180deg,#d9cfc2 0%,#c3b29d 45%,#4a4a52 100%);border-radius:120px 120px 0 0"></div>
  <div class="photo" role="img" aria-label="Photo of the Eiffel Tower under a blue sky" style="left:558px;top:131px;width:106px;height:106px;background:linear-gradient(180deg,#7fc0e6,#3b7fa6)"></div>
  <div class="photo" role="img" aria-label="Photo of the Arc de Triomphe at night" style="left:899px;top:94px;width:128px;height:128px;background:radial-gradient(circle,#d8a44a 0%,#6b4a2a 45%,#0d1a3d 80%)"></div>
  <div class="photo" role="img" aria-label="Photo of the Louvre glass pyramid" style="left:446px;top:378px;width:196px;height:196px;background:linear-gradient(180deg,#b8dbef 0%,#8fa7b5 50%,#3d5a6c 100%)"></div>

  <!-- services -->
  <section class="services">
    <div class="kicker" style="top:47px">The 7 Parts Of Our Business</div>
    <h2 class="section-title" style="top:66px;color:var(--accent)">Our Services</h2>

    <svg class="abs" style="left:348px;top:114px" width="348" height="348" viewBox="0 0 348 348">
      <circle cx="174" cy="174" r="172" fill="none" stroke="#d6d6d6" stroke-width="1.3" stroke-dasharray="6 6"/>
      <circle cx="174" cy="174" r="140" fill="#2c2c2c"/>
      <circle cx="174" cy="174" r="92" fill="#fff"/>
      <text x="174" y="170" text-anchor="middle" font-family="Inter,sans-serif" font-weight="700" font-size="15" fill="#0b3a8f">Pelican</text>
      <text x="174" y="189" text-anchor="middle" font-family="Inter,sans-serif" font-weight="700" font-size="15" fill="#0b3a8f">Global</text>
    </svg>

    <div class="svc-icon" style="left:323px;top:152px;background:#2b2438"><div style="background:var(--purple)"><svg viewBox="0 0 24 24"><rect x="4" y="3" width="16" height="18" rx="2"/><circle cx="12" cy="11" r="4"/><path d="M12 7v8M8 11h8"/></svg></div></div>
    <div class="svc" style="left:105px;top:132px"><h3>Visa Services</h3><p>Lorem ipsum dolor sit amet elit consetr adipiscing elit</p></div>

    <div class="svc-icon" style="left:720px;top:152px;background:#1b2436"><div style="background:#1d4d9c"><svg viewBox="0 0 24 24"><path d="M3 20V9l9-5 9 5v11"/><path d="M6 20v-6h12v6M6 17h12"/><circle cx="9" cy="12" r="1.3"/></svg></div></div>
    <div class="svc" style="left:792px;top:132px"><h3>International Hotel Reservation</h3><p>Lorem ipsum dolor sit amet elit consetr adipiscing elit</p></div>

    <div class="svc-icon" style="left:274px;top:288px;background:#3a2220"><div style="background:var(--red)"><svg viewBox="0 0 24 24"><path d="M12 3l9 5-9 5-9-5z"/><path d="M3 12l9 5 9-5M3 16l9 5 9-5"/></svg></div></div>
    <div class="svc" style="left:62px;top:262px;width:170px"><h3>International Business Resources</h3><p>Lorem ipsum dolor sit amet elit consetr adipiscing elit</p></div>

    <div class="svc-icon" style="left:764px;top:288px;background:#352c17"><div style="background:var(--gold)"><svg viewBox="0 0 24 24"><path d="M3 7h18v3a2 2 0 0 0 0 4v3H3v-3a2 2 0 0 0 0-4z"/><path d="M14 7v10" stroke-dasharray="2 2"/></svg></div></div>
    <div class="svc" style="left:822px;top:268px"><h3>Worldwide Flight Tickets Booking</h3><p>Lorem ipsum dolor sit amet elit consetr adipiscing elit</p></div>

    <div class="svc-icon" style="left:323px;top:442px;background:#202c1e"><div style="background:var(--green)"><svg viewBox="0 0 24 24"><path d="M5 8h14l-1 13H6z"/><path d="M9 8V6a3 3 0 0 1 6 0v2"/></svg></div></div>
    <div class="svc" style="left:105px;top:432px"><h3>Duty Free Goods</h3><p>Lorem ipsum dolor sit amet elit consetr adipiscing elit</p></div>

    <div class="svc-icon" style="left:720px;top:442px;background:#172d2f"><div style="background:var(--teal)"><svg viewBox="0 0 24 24"><circle cx="12" cy="12" r="9"/><path d="M3 12h18M12 3c3 3 3 15 0 18M12 3c-3 3-3 15 0 18"/></svg></div></div>
    <div class="svc" style="left:779px;top:432px"><h3>Worldwide Travel Arrangement</h3><p>Lorem ipsum dolor sit amet elit consetr adipiscing elit</p></div>

    <div class="svc-icon" style="left:522px;top:519px;background:#372414"><div style="background:var(--orange)"><svg viewBox="0 0 24 24"><path d="M4 19h16l1-12-5 4-4-6-4 6-5-4z"/><circle cx="12" cy="14" r="1"/></svg></div></div>
    <div class="svc" style="left:422px;top:585px;width:200px;text-align:center"><h3>VIP Airport Concierge</h3><p>Lorem ipsum dolor sit amet elit consetr adipiscing elit</p></div>
  </section>

  <!-- destinations map -->
  <section class="map-sec">
    <div class="kicker" style="top:50px;color:#888">Discover The Most Popular Destinations</div>
    <h2 class="section-title" style="top:69px;color:var(--navy)">Business Resources Cities</h2>
    <div class="map-area" role="img" aria-label="Watercolour world map with continents coloured by region"></div>
    <div class="view" style="left:100px;top:201px"><i></i>View Cities</div>
    <div class="view" style="left:436px;top:201px"><i></i>View Cities</div>
    <div class="view" style="left:589px;top:226px"><i></i>View Cities</div>
    <div class="view" style="left:401px;top:323px"><i></i>View Cities</div>
    <div class="view" style="left:212px;top:381px"><i></i>View Cities</div>
    <div class="view" style="left:715px;top:444px"><i></i>View Cities</div>
    <div class="legend">
      <div style="color:#6b3fc4"><svg viewBox="0 0 24 34"><path d="M12 33C4 20 2 16 2 11a10 10 0 0 1 20 0c0 5-2 9-10 22z" fill="#8a5bd6"/><circle cx="12" cy="11" r="6" fill="#fff"/><text x="12" y="14" font-size="8" text-anchor="middle" fill="#8a5bd6" font-family="Inter,sans-serif">1</text></svg>North America</div>
      <div style="color:#5e9d2e"><svg viewBox="0 0 24 34"><path d="M12 33C4 20 2 16 2 11a10 10 0 0 1 20 0c0 5-2 9-10 22z" fill="#6bb040"/><circle cx="12" cy="11" r="6" fill="#fff"/><text x="12" y="14" font-size="8" text-anchor="middle" fill="#6bb040" font-family="Inter,sans-serif">2</text></svg>South America</div>
      <div style="color:#e6a23a"><svg viewBox="0 0 24 34"><path d="M12 33C4 20 2 16 2 11a10 10 0 0 1 20 0c0 5-2 9-10 22z" fill="#e6a23a"/><circle cx="12" cy="11" r="6" fill="#fff"/><text x="12" y="14" font-size="8" text-anchor="middle" fill="#e6a23a" font-family="Inter,sans-serif">4</text></svg>Africa</div>
      <div style="color:#3f86d6"><svg viewBox="0 0 24 34"><path d="M12 33C4 20 2 16 2 11a10 10 0 0 1 20 0c0 5-2 9-10 22z" fill="#5aa0e0"/><circle cx="12" cy="11" r="6" fill="#fff"/><text x="12" y="14" font-size="8" text-anchor="middle" fill="#5aa0e0" font-family="Inter,sans-serif">3</text></svg>Europe</div>
      <div style="color:#e8902e"><svg viewBox="0 0 24 34"><path d="M12 33C4 20 2 16 2 11a10 10 0 0 1 20 0c0 5-2 9-10 22z" fill="#eb9a3d"/><circle cx="12" cy="11" r="6" fill="#fff"/><text x="12" y="14" font-size="8" text-anchor="middle" fill="#eb9a3d" font-family="Inter,sans-serif">6</text></svg>Australia</div>
      <div style="color:#d9356b"><svg viewBox="0 0 24 34"><path d="M12 33C4 20 2 16 2 11a10 10 0 0 1 20 0c0 5-2 9-10 22z" fill="#e3507d"/><circle cx="12" cy="11" r="6" fill="#fff"/><text x="12" y="14" font-size="8" text-anchor="middle" fill="#e3507d" font-family="Inter,sans-serif">5</text></svg>Asia</div>
    </div>
    <a class="btn" style="left:455px;top:581px;width:135px;height:27px;background:#1657c8">View All Cities <svg viewBox="0 0 10 10"><path d="M3 1l4 4-4 4" stroke="#fff" stroke-width="1.6" fill="none"/></svg></a>
  </section>

  <!-- testimonials -->
  <section class="testi">
    <div class="kicker" style="top:40px;color:var(--orange)">What Others Say About Us</div>
    <h2 class="section-title" style="top:58px">Testimonials</h2>
    <article class="t-card" style="left:109px">
      <div class="t-head"><div class="avatar" role="img" aria-label="Portrait of Adam Smith"></div><div><div class="t-name">Adam Smith</div><div class="t-role">CEO</div></div></div>
      <p>Lorem ipsum dolor sit amet consectetur adipiscing elit Ut et massa mi. Aliquam in hendrerit urna. Pellentesque sit amet sapien fringilla, mattis ligula consectetur</p>
      <div class="quote">”</div>
    </article>
    <article class="t-card" style="left:408px">
      <div class="t-head"><div class="avatar" role="img" aria-label="Portrait of Jane Smith" style="background:linear-gradient(135deg,#caa58a,#3b2a22)"></div><div><div class="t-name">Jane Smith</div><div class="t-role">Youtuber</div></div></div>
      <p>Lorem ipsum dolor sit amet consectetur adipiscing elit Ut et massa mi. Aliquam in hendrerit urna. Pellentesque sit amet sapien fringilla, mattis ligula consectetur</p>
      <div class="quote">”</div>
    </article>
    <article class="t-card" style="left:706px">
      <div class="t-head"><div class="avatar" role="img" aria-label="Portrait of Meriam Elit" style="background:linear-gradient(135deg,#4a2b3a,#140c10)"></div><div><div class="t-name">Meriam Elit</div><div class="t-role">Blogger</div></div></div>
      <p>Lorem ipsum dolor sit amet consectetur adipiscing elit Ut et massa mi. Aliquam in hendrerit urna. Pellentesque sit amet sapien fringilla, mattis ligula consectetur</p>
      <div class="quote">”</div>
    </article>
  </section>

  <!-- footer -->
  <footer class="footer">
    <div class="brand" style="left:51px;top:42px">
      <div class="brand-mark" style="width:40px;height:40px"></div>
      <div class="brand-name" style="width:130px">Pelican Global Trade &amp; Heritage Forum</div>
    </div>
    <p class="f-text">Lorem ipsum dolor sit amet consectetur adipiscing elit Ut et massa mi. Aliquam in hendrerit urna. Pellentesque sit amet sapien fringilla, mattis ligula consectetur</p>

    <div class="f-col" style="left:420px;width:160px"></div>
    <div class="f-head" style="left:446px;top:56px">Sitemap</div>
    <div class="f-link" style="left:449px;top:92px">Home</div>
    <div class="f-link" style="left:449px;top:123px">Worldmap</div>
    <div class="f-link" style="left:449px;top:151px">Services</div>
    <div class="f-link" style="left:449px;top:179px">FAQ</div>

    <div class="f-col" style="left:596px;width:200px"></div>
    <div class="f-head" style="left:621px;top:56px">Important Links</div>
    <div class="f-link" style="left:625px;top:92px">Contact Us</div>
    <div class="f-link" style="left:625px;top:123px">About Us</div>
    <div class="f-link" style="left:625px;top:151px">Terms and Conditions</div>
    <div class="f-link" style="left:625px;top:179px">Copyright Notice</div>

    <div class="f-col" style="left:821px;width:200px;height:50px"></div>
    <div class="f-head" style="left:844px;top:70px;font-size:11px">Start Today</div>
    <a class="btn" style="left:844px;top:91px;width:106px;height:27px;background:#1657c8">Booking <svg viewBox="0 0 10 10"><path d="M3 1l4 4-4 4" stroke="#fff" stroke-width="1.6" fill="none"/></svg></a>
    <div class="f-head" style="left:844px;top:171px;font-size:11px">Talk to us?</div>
    <a class="btn" style="left:844px;top:192px;width:121px;height:27px;background:#f1f2f4;color:#222">Contact Us <svg viewBox="0 0 10 10"><path d="M3 1l4 4-4 4" stroke="#222" stroke-width="1.6" fill="none"/></svg></a>

    <div class="social">
      <span><i></i>ProNet</span>
      <span><i></i>FriendHub</span>
      <span><i></i>Chirper</span>
    </div>
    <div class="copy">Copyright © 2023 PELICAN GLOBAL TRADE &amp; HERITAGE FORUM. All rights reserved.</div>
  </footer>
</main>
</body>
</html>
```